Mechanical Engineer Business Card Design (Unemployed)

I am unemployed and actively looking for a job in Canada. I will be using this business card when I meet potential employers or in networking events.I would love to have the engraved writing style (as if it is engraved on the card). Some examples attached.I would love to have a personalized logo that represents my 2 majors. The final design should have a professional look that can stand out if attached to a resume. Jobs I am applying for are in construction, mining, oil and gas, Aerospace, manufacturing and whatever field I can be integrated in.A metallic look on the back is ok. but the front have to be sort of can be written on. you can also try to add my linkedin profile https://ca.folionet.example/in/doruvelsh
On the front or back, I would love to have the symbol of mail and phone rather than the words. that saves spaceAmaze me guys.

Target Market(s)

Engineering

Industry/Entity Type

Engineering

Contact Information for Business Card

Doru Velsh
Mechanical Engineer

Phone number: +1 (555) 014 - 2736
email: velshdoru@mailbrook.example

Font styles to use
Serif
Sans Serif
Decorative
Script

Requirements
Must have
• PERSONALIZED and brand new Simple Logo
• Professional look
• Engraved writing for the name
• Help stand out when attached on CV
Nice to have
• Metallic back look

```html
<!DOCTYPE html>
<html lang="en">
<head>
<meta charset="utf-8">
<title>Doru Velsh — Business Card</title>
<link rel="stylesheet" href="https://fonts.googleapis.com/css2?family=Open+Sans:wght@300;400&display=swap">
<style>
  :root {
    --page-bg: #e9e7e3;
    --card-light: #f4f4f4;
    --card-mid: #dcdcdc;
    --card-dark: #c4c4c4;
    --ink: #2b2b2b;
    --ink-soft: #4a4a4a;
    --engrave-light: rgba(255,255,255,0.9);
    --engrave-dark: rgba(0,0,0,0.35);
    --mark: #111111;
  }
  html, body {
    margin: 0;
    width: 1200px;
    height: 892px;
    overflow: hidden;
    background: var(--page-bg);
    font-family: "Open Sans", Arial, sans-serif;
  }
  .sheet {
    position: relative;
    width: 1200px;
    height: 892px;
    display: flex;
    flex-direction: column;
    align-items: center;
    justify-content: center;
    gap: 40px;
  }
  .card {
    position: relative;
    width: 660px;
    height: 377px;
    border-radius: 3px;
    background: radial-gradient(ellipse at 35% 30%, var(--card-light) 0%, var(--card-mid) 60%, var(--card-dark) 100%);
    box-shadow: 0 8px 22px rgba(0,0,0,0.22), 0 1px 2px rgba(0,0,0,0.2);
    overflow: hidden;
  }
  .engraved {
    color: var(--ink);
    text-shadow: 0 1px 0 var(--engrave-light), 0 -1px 0 var(--engrave-dark);
  }
  .identity {
    position: absolute;
    left: 44px;
    top: 120px;
  }
  .identity__name {
    margin: 0;
    font-size: 40px;
    font-weight: 400;
    letter-spacing: 0.5px;
    line-height: 1;
  }
  .identity__role {
    margin: 8px 0 0;
    font-size: 19px;
    font-weight: 400;
    color: var(--ink-soft);
  }
  .identity__degree {
    margin: 2px 0 0;
    font-size: 14px;
    font-weight: 300;
    color: var(--ink-soft);
  }
  .contact {
    position: absolute;
    left: 44px;
    bottom: 40px;
    list-style: none;
    margin: 0;
    padding: 0;
    font-size: 18px;
    font-weight: 300;
  }
  .contact__item {
    display: flex;
    align-items: center;
    gap: 10px;
    margin-top: 6px;
  }
  .contact__icon {
    width: 14px;
    height: 14px;
    flex: none;
  }
  .brand {
    position: absolute;
    display: flex;
    align-items: center;
    gap: 12px;
    color: var(--mark);
    font-weight: 400;
  }
  .brand__dot {
    border-radius: 50%;
    background: var(--mark);
    flex: none;
  }
  .card--front .brand {
    right: 48px;
    top: 70px;
    font-size: 30px;
  }
  .card--front .brand__dot { width: 16px; height: 16px; }
  .card--back {
    background: linear-gradient(160deg, #fafafa 0%, #e2e2e2 45%, #cfcfcf 75%, #e6e6e6 100%);
  }
  .card--back .brand {
    left: 50%;
    top: 50%;
    transform: translate(-50%, -50%);
    font-size: 44px;
  }
  .card--back .brand__dot { width: 22px; height: 22px; }
</style>
</head>
<body>
<main class="sheet">
  <section class="card card--front" aria-label="Card front">
    <div class="brand">
      <span class="brand__dot"></span>
      <span class="brand__name">Doru Velsh</span>
    </div>
    <div class="identity">
      <h1 class="identity__name engraved">Doru Velsh</h1>
      <p class="identity__role engraved">Field Mechanical Engineer</p>
      <p class="identity__degree engraved">Mechanical Engineer (B.Sc.)</p>
      <p class="identity__degree engraved">Aerospace Engineer (M.Sc.)</p>
    </div>
    <ul class="contact">
      <li class="contact__item engraved">
        <svg class="contact__icon" viewBox="0 0 14 14" aria-label="Phone">
          <rect width="14" height="14" fill="#ffffff"/>
          <path d="M4 2.5 L5.6 4.6 L4.8 5.6 C5.4 7 6.6 8.3 8.2 9 L9.2 8.2 L11.4 9.8 L10.4 11.5 C6.5 11.2 2.8 7.4 2.5 3.6 Z" fill="#222"/>
        </svg>
        <span>(+1) 555 - 014 - 2736</span>
      </li>
      <li class="contact__item engraved">
        <svg class="contact__icon" viewBox="0 0 14 14" aria-label="Email">
          <rect width="14" height="14" fill="#ffffff"/>
          <rect x="2" y="3.5" width="10" height="7" fill="#222"/>
          <path d="M2 3.5 L7 7.5 L12 3.5" fill="none" stroke="#ffffff" stroke-width="0.9"/>
        </svg>
        <span>velshdoru@mailbrook.example</span>
      </li>
    </ul>
  </section>

  <section class="card card--back" aria-label="Card back">
    <div class="brand">
      <span class="brand__dot"></span>
      <span class="brand__name">Doru Velsh</span>
    </div>
  </section>
</main>
</body>
</html>
```